Thank You For Shopping / Hair Care Tips

I need “Thank You For Shopping”
Post cards made for my hair business !
I added pictures of post cards that I really like . I also added my LuzeKora Wigs logo for you guys to use

I want the backside of the flyer to have hair care tips !
I want people to have full directions on how to care for their wigs

Target Market(s)

Im marking to young woman to older middle aged woman
Ages 23-66 . I want my flyer to look mature And classy

Industry/Entity Type

Hair And Beauty

Font styles to use
Serif
Script

Colors
e34699
e34298
e34398

Requirements
Must have
• The flyer must have the Instagram logo with my Instagram name next to it @luze.kora.wigs__
• Also it must have my “Luze Kora Wigs” logo that I’ve uploaded in the pictures section .
• Flyer had to be two sides . One side “ thank you for shopping “ side two “hair care tips”
• My website must be on the flyer - www.luzekorawigs.example
• The flyer must match the colors of my logo
• All white . With the pink and glitter sliver you see on my logo
Nice to have
• Nice to have a glitter border
Should not have
• The flyer should not have different colors that don’t match my logo
• It shouldn’t be made without having my Instagram or website on the flyer

```html
<!DOCTYPE html>
<html lang="en">
<head>
<meta charset="utf-8">
<title>Luze Kora Wigs – Thank You Postcards</title>
<link href="https://fonts.googleapis.com/css2?family=Great+Vibes&family=Tinos:wght@400;700&display=swap" rel="stylesheet">
<style>
  :root {
    --pink: #e34699;
    --pink-deep: #e34298;
    --card-white: #f3f3f3;
    --page: #ece8eb;
    --rule: #e34398;
  }
  * { box-sizing: border-box; margin: 0; padding: 0; }
  html, body { width: 1200px; height: 1200px; overflow: hidden; }
  body {
    background: var(--page);
    position: relative;
    font-family: "Tinos", "Times New Roman", serif;
  }
  .postcard {
    position: absolute;
    left: 245px;
    width: 710px;
    height: 545px;
    background: var(--pink);
    padding: 18px;
  }
  .postcard--front { top: 42px; }
  .postcard--back { top: 613px; }
  .postcard__face {
    position: relative;
    width: 100%;
    height: 100%;
    background: var(--card-white);
  }
  .front__title {
    position: absolute;
    top: 40px;
    left: 0;
    right: 0;
    text-align: center;
    font-family: "Great Vibes", cursive;
    color: var(--pink);
    font-size: 78px;
    line-height: 1;
  }
  .brand-name {
    color: var(--pink);
    font-family: "Tinos", "Times New Roman", serif;
    font-weight: 400;
    white-space: nowrap;
  }
  .front__brand {
    position: absolute;
    top: 245px;
    left: 0;
    right: 0;
    text-align: center;
    font-size: 62px;
  }
  .front__rule {
    position: absolute;
    left: 0;
    right: 0;
    top: 440px;
    height: 3px;
    background: var(--rule);
  }
  .front__contacts {
    position: absolute;
    left: 22px;
    right: 28px;
    top: 458px;
    display: flex;
    justify-content: space-between;
    align-items: center;
    font-weight: 700;
    font-size: 21px;
    color: var(--pink);
  }
  .contact { display: flex; align-items: center; gap: 10px; }
  .contact svg { display: block; }
  .back__tips {
    position: absolute;
    top: 88px;
    left: 86px;
    list-style: none;
    color: var(--pink);
    font-size: 31px;
    line-height: 37px;
  }
  .back__tips li::before { content: "- "; }
  .back__brand {
    position: absolute;
    right: 26px;
    bottom: 26px;
    font-size: 24px;
  }
</style>
</head>
<body>
  <section class="postcard postcard--front" aria-label="Front of postcard">
    <div class="postcard__face">
      <h1 class="front__title">Thank You For Shopping</h1>
      <p class="brand-name front__brand">Luze Kora Wigs</p>
      <div class="front__rule"></div>
      <div class="front__contacts">
        <span class="contact">
          <svg width="30" height="30" viewBox="0 0 30 30" aria-hidden="true">
            <rect x="2" y="2" width="26" height="26" rx="6" fill="none" stroke="#e34699" stroke-width="3"/>
          </svg>
          @luze.kora.wigs__
        </span>
        <span class="contact">
          <svg width="30" height="30" viewBox="0 0 30 30" aria-hidden="true">
            <circle cx="15" cy="15" r="12.5" fill="none" stroke="#e34699" stroke-width="3"/>
          </svg>
          www.luzekorawigs.example
        </span>
      </div>
    </div>
  </section>

  <section class="postcard postcard--back" aria-label="Back of postcard: hair care tips">
    <div class="postcard__face">
      <ul class="back__tips">
        <li>Detangle gently with conditioner</li>
        <li>Trim split ends regularly</li>
        <li>Do oil pre-poss</li>
        <li>Let air dry</li>
        <li>Keep moisturized</li>
        <li>Utilize protective style</li>
        <li>Avoid heat styling hair</li>
        <li>Apply protein treatment</li>
        <li>Use wide-tooth combs</li>
      </ul>
      <p class="brand-name back__brand">Luze Kora Wigs</p>
    </div>
  </section>
</body>
</html>
```